Stationery and business cards - New design

I need following designs
- writing paper for business letters A4, you can take the data from our old paper. There should just be a place for a third bank account.
- writing paper for business letters (only design + logo, without address, bank accounts and legal data)
- business cards with qr code, one side, only German language (you can take the data from the old layout)

Target Market(s)

Industrial customers

Industry/Entity Type

sheet metal technology, laser cutting of metal sheet

Requirements
Must have
• The address above the recipient should be placed like on my old paper. No relationship to the old design (only color) - please make a completely new design.
Nice to have
• colors like in my new logo
Should not have
• - the business letter should be suitable for borderless print - the green timber in my old paper is very bad for this - so please make a design without a timber (or a timber like it is on my old paper)

```html
<!DOCTYPE html>
<html lang="de">
<head>
<meta charset="utf-8">
<title>Waldegg Blechtechnik – Briefbogen</title>
<link rel="stylesheet" href="https://fonts.googleapis.com/css2?family=Montserrat:wght@500;600;700&display=swap">
<style>
  :root {
    --brand-blue: #00468a;
    --brand-teal: #008691;
    --paper: #fefefe;
    --white: #ffffff;
  }
  * { margin: 0; padding: 0; box-sizing: border-box; }
  html, body { width: 850px; height: 1200px; overflow: hidden; background: var(--paper); }
  .letterhead {
    position: relative;
    width: 850px;
    height: 1200px;
    background: var(--paper);
    font-family: "Montserrat", sans-serif;
    color: var(--brand-blue);
  }
  .brand {
    position: absolute;
    left: 528px;
    top: 57px;
    display: flex;
    align-items: center;
    gap: 14px;
  }
  .brand-dot {
    width: 56px;
    height: 56px;
    border-radius: 50%;
    background: var(--brand-teal);
  }
  .brand-name {
    font-weight: 700;
    font-size: 25px;
    line-height: 1.05;
    letter-spacing: 0.5px;
    color: var(--brand-blue);
  }
  .brand-name span { display: block; }
  .sender {
    position: absolute;
    left: 580px;
    top: 154px;
    font-weight: 600;
    font-size: 14.5px;
    line-height: 15.5px;
    color: var(--brand-blue);
  }
  .footer-shape { position: absolute; left: 0; top: 0; width: 850px; height: 1200px; pointer-events: none; }
  .contact {
    position: absolute;
    display: flex;
    align-items: center;
    gap: 10px;
    font-weight: 500;
    font-size: 17.5px;
    letter-spacing: 0.6px;
    color: var(--white);
  }
  .contact svg { width: 18px; height: 18px; flex: none; }
  .contact-phone { left: 151px; top: 1098px; }
  .contact-fax   { left: 151px; top: 1126px; }
  .contact-mail  { left: 466px; top: 1098px; }
  .contact-web   { left: 466px; top: 1127px; }
  .footer-mark {
    position: absolute;
    left: 751px;
    top: 1104px;
    width: 58px;
    height: 58px;
    border-radius: 50%;
    border: 4px solid var(--white);
  }
</style>
</head>
<body>
<main class="letterhead">
  <header class="brand">
    <div class="brand-dot" aria-hidden="true"></div>
    <div class="brand-name"><span>WALDEGG</span><span>BLECHTECHNIK</span></div>
  </header>

  <address class="sender" style="font-style:normal">
    Waldegg Blechtechnik GmbH<br>
    Talweg-Süd 4<br>
    D-93170 Bernau
  </address>

  <svg class="footer-shape" viewBox="0 0 850 1200" aria-hidden="true">
    <path fill="var(--brand-teal)" d="M0 1071 H416 C406 1072 400 1076 396 1083 H0 Z"/>
    <path fill="var(--brand-blue)" d="M0 1087 H404 C410 1077 422 1071 442 1071 H850 V1200 H0 Z"/>
  </svg>

  <div class="contact contact-phone">
    <svg viewBox="0 0 18 18"><rect width="18" height="18" rx="2" fill="#fff"/><path d="M5 14 C4 10 8 5 12 4 L13.5 5.5 L11.5 7 L10.5 6.5 C8.5 8 7.5 9.5 7 11.5 L8 12.3 L6.5 14.5 Z" fill="var(--brand-blue)"/></svg>
    <span>+49(0)941577320-0</span>
  </div>
  <div class="contact contact-fax">
    <svg viewBox="0 0 18 18"><rect width="18" height="18" rx="2" fill="#fff"/><rect x="6" y="3" width="6" height="5" fill="none" stroke="var(--brand-blue)" stroke-width="1.2"/><rect x="4" y="8" width="10" height="6" fill="var(--brand-blue)"/><rect x="6" y="11" width="6" height="1.2" fill="#fff"/></svg>
    <span>+49(0)941577320-318</span>
  </div>
  <div class="contact contact-mail">
    <svg viewBox="0 0 18 18"><rect width="18" height="18" rx="2" fill="#fff"/><rect x="3.5" y="5.5" width="11" height="7.5" fill="none" stroke="var(--brand-blue)" stroke-width="1.3"/><path d="M3.5 5.5 L9 10 L14.5 5.5" fill="none" stroke="var(--brand-blue)" stroke-width="1.3"/></svg>
    <span>info@waldegg-blt.de</span>
  </div>
  <div class="contact contact-web">
    <svg viewBox="0 0 18 18"><rect width="18" height="18" rx="2" fill="#fff"/><circle cx="9" cy="9" r="5" fill="none" stroke="var(--brand-blue)" stroke-width="1.3"/><path d="M4 9 H14 M9 4 C6.5 6.5 6.5 11.5 9 14 M9 4 C11.5 6.5 11.5 11.5 9 14" fill="none" stroke="var(--brand-blue)" stroke-width="1"/></svg>
    <span>www.waldegg-blt.de</span>
  </div>

  <div class="footer-mark" aria-hidden="true"></div>
</main>
</body>
</html>
```